Brell Harbor Company Business Cards

Front and Back Business Card - logo and text setup - cool design. I need workable photoshop or illustrator files so I can setup each employee card with design that is created
Updates

Hi everyone, thank you for the great entries. Please no more white and blue cards - there are so many already - black and silver only now please. thanks!

Target Market(s)

Construction Industry - Facility Managers

Industry/Entity Type

Construction

Contact Information for Business Card

I really like contemporary simplistic looks - clean neat....not opposed to seeing some black backrounds

Requirements
Must have
• Logo/website address with design on front only - www.brellharbor-example.com (logo attached)
• Back:
• Name/Title/Company Address/Phone/email address
Nice to have
• Cool design
Should not have
• Nothing gimmicky like Fire or Water - since we are a Fire Protection company - it has all been done

```html
<!DOCTYPE html>
<html lang="en">
<head>
<meta charset="utf-8">
<title>Brell Harbor Company – Business Cards</title>
<link href="https://fonts.googleapis.com/css2?family=Work+Sans:wght@400;500;800&display=swap" rel="stylesheet">
<style>
  :root {
    --black: #141517;
    --charcoal: #26282c;
    --silver: #c9ccd1;
    --silver-light: #e6e8eb;
    --silver-dark: #8d9198;
    --ink: #2b2d31;
    --muted: #5f636a;
    --stage: #e9eaec;
  }
  * { margin: 0; padding: 0; box-sizing: border-box; }
  html, body {
    width: 1200px; height: 900px; overflow: hidden;
    background: var(--stage);
    font-family: "Work Sans", Arial, sans-serif;
  }
  .sheet {
    width: 1200px; height: 900px;
    display: flex; flex-direction: column;
    align-items: center; justify-content: center; gap: 60px;
  }
  .card {
    position: relative;
    width: 525px; height: 300px;
    overflow: hidden;
    box-shadow: 0 10px 28px rgba(0,0,0,.22);
  }
  .brand { display: flex; align-items: center; gap: 10px; }
  .brand__mark { width: 14px; height: 14px; background: var(--silver); flex: none; }
  .brand__name { font-weight: 800; line-height: 1; letter-spacing: -0.5px; }

  /* Front: logo and website */
  .card--front {
    background: radial-gradient(circle at 40% 35%, var(--charcoal) 0%, var(--black) 100%);
    display: flex; flex-direction: column; align-items: center; justify-content: center;
    padding-bottom: 40px;
  }
  .card--front .brand { gap: 16px; }
  .card--front .brand__mark { width: 22px; height: 22px; }
  .card--front .brand__name { font-size: 54px; color: var(--silver); }
  .website {
    margin-top: 16px; font-size: 14px; font-weight: 500;
    letter-spacing: 1.5px; color: var(--silver-dark);
  }

  /* Back: name, title, address, phone, email */
  .card--back { background: linear-gradient(160deg, #ffffff 0%, var(--silver-light) 100%); }
  .card--back .brand { position: absolute; left: 38px; top: 36px; }
  .card--back .brand__mark { background: var(--black); }
  .card--back .brand__name { font-size: 30px; color: var(--black); }
  .person { position: absolute; right: 40px; top: 98px; text-align: right; }
  .person__name {
    font-weight: 500; font-size: 20px; color: var(--black);
    letter-spacing: 1.5px; text-transform: uppercase;
  }
  .person__title { font-size: 13px; color: var(--muted); margin-top: 2px; }
  .divider {
    position: absolute; left: 30px; right: 34px; top: 150px;
    height: 1.5px; background: var(--silver-dark);
  }
  .contacts {
    position: absolute; left: 38px; top: 164px;
    list-style: none; font-size: 12.5px; color: var(--ink); line-height: 1.6;
  }
  .contacts li { display: flex; align-items: center; gap: 8px; }
  .contacts svg { width: 10px; height: 10px; flex: none; }
  .address {
    position: absolute; right: 40px; top: 164px; text-align: right;
    font-size: 12.5px; color: var(--ink); line-height: 1.6;
  }
  .wave { position: absolute; left: 0; bottom: 0; width: 525px; height: 300px; }
</style>
</head>
<body>
<main class="sheet">
  <section class="card card--front" aria-label="Card front">
    <div class="brand">
      <span class="brand__mark"></span>
      <span class="brand__name">Brell Harbor</span>
    </div>
    <p class="website">www.brellharbor-example.com</p>
    <svg class="wave" viewBox="0 0 525 300" aria-hidden="true">
      <path d="M0 262 C150 270 260 258 370 274 C440 284 490 290 525 298 L525 300 L0 300 Z" fill="#3a3d42"/>
      <path d="M0 255 C150 263 260 251 370 267 C440 277 490 284 525 292" fill="none" stroke="var(--silver)" stroke-width="2.5"/>
    </svg>
  </section>

  <section class="card card--back" aria-label="Card back">
    <div class="brand">
      <span class="brand__mark"></span>
      <span class="brand__name">Brell Harbor</span>
    </div>
    <div class="person">
      <p class="person__name">Daniel Varga</p>
      <p class="person__title">Director</p>
    </div>
    <div class="divider"></div>
    <ul class="contacts">
      <li><svg viewBox="0 0 10 10"><path d="M2 0.5 L3.6 2.6 L2.8 3.6 Q4 6 6.4 7.2 L7.4 6.4 L9.5 8 L8.4 9.5 Q2 8.5 0.5 1.6 Z" fill="#141517"/></svg>(555) 014-2869</li>
      <li><svg viewBox="0 0 10 10"><rect x="1" y="3" width="8" height="5" rx="1" fill="#141517"/><rect x="3" y="0.5" width="4" height="2.5" fill="#141517"/></svg>(555) 014-2866</li>
      <li><svg viewBox="0 0 10 10"><path d="M0.5 2 H9.5 V8 H0.5 Z M1.2 2.6 L5 5.4 L8.8 2.6" fill="none" stroke="#141517" stroke-width="1"/></svg>info@brellharbor-example.com</li>
    </ul>
    <div class="address">
      <p>48 Quarry Lane</p>
      <p>Westbrook, ME 04092</p>
    </div>
    <svg class="wave" viewBox="0 0 525 300" aria-hidden="true">
      <path d="M0 262 C150 270 260 258 370 274 C440 284 490 290 525 298 L525 300 L0 300 Z" fill="var(--black)"/>
      <path d="M0 255 C150 263 260 251 370 267 C440 277 490 284 525 292" fill="none" stroke="var(--silver-dark)" stroke-width="2.5"/>
    </svg>
  </section>
</main>
</body>
</html>
```